Website and Logo Design for new niche job board.

Hello, We are an up and coming job board that is focused on LEGITIMATE companies that hire telecommuters to work from home. We are looking to build a highly interactive job board and forum/blog. The site is called WorkHarbor.com We focus on helping work at home moms, older workers and college students in work at home positions. We offer free job posting and advertising to the employer and free resume posting to the job seeker. (Free everything basically) Our revenue will be based from banner ads on the site so we will need a space on both sides of the page for those ads. 

The software we are using to build the job board part of the site can be viewed at www.pavloquill.example. It is already built! We do not need job software but a dashboard look to our main page - PLEASE pay attention to this! Do not submit a job board look as we have the job board page built!

These are the sites I like - please use these links to understand exactly the look I want

 

http://www.brightmarmots.example/

http://www.tessvoran.example/

http://www.ladiesatlabor.example/

https://www.findingnannies.example/index.asp?
Updates

Hi everyone- I think there might be some confusion to what we are looking for. We have the job board software through www.pavloquill.example, we are looking for the main page to be built around that. Basically we want a dashboard look with lots of little boxes to add content such as different articles,podcasts, forums,blogs,highlight different companies hiring,etc. If you can add scrolling or moving objects would be ideal. The less of a static website the better. You dont have to worry about the jobboard portion just the main page when you click on www.WorkHarbor.com, we really need it to capture peoples attention and see its a staffing firm AND a job board, forum, etc for work at home positions.  Here are some looks I am aiming for -

http://www.tessvoran.example/

Please use alot of color- lime green, oranges, turquiose blue, purple, lots and lots of color please! I like more tropical colors. Thanks! I dont like red and dark colors at all. Thanks

Target Market(s)

Target customers will be both companies and individuals. The individuals will be a broad age range that are interested in working from home. The companies will be small to large corporations that have valid work from home positions.

Requirements
Must have
• I want a colorful site with moving objects and scrolling text - static sites are bland, and outdated- I am looking for a HIGHLY interactive board. Please do not just throw a template up there and expect me to like it. I am picky and want an ultra sleek design and eye catching. I can make an out of the box website myself, I have 3 other companies and did that -  PLEASE PLEASE DO NOT SHOW ME A COOKIE!
Nice to have
• Would be very nice to have the HTML sliced up for finished designs.
Should not have
• just not boring and static. Anything new and creative is where we are heading.

```html
<!DOCTYPE html>
<html lang="en">
<head>
<meta charset="utf-8">
<title>WorkHarbor.com – Work From Home Jobs</title>
<link rel="stylesheet" href="https://fonts.googleapis.com/css2?family=Ubuntu:wght@400;500;700&family=Noto+Sans:wght@400;700&display=swap">
<style>
:root{
  --lime:#b3f000;
  --grass:#78ad12;
  --grass-dark:#649a0a;
  --magenta:#e0107b;
  --orange:#ff6a00;
  --turquoise:#22b0d8;
  --purple:#9b16b0;
  --slate:#6a6a6a;
  --ink:#1a1a1a;
  --paper:#ffffff;
  --mist:#f4f4f4;
  --rule:#d8d8d8;
}
*{box-sizing:border-box;margin:0;padding:0}
html,body{width:1017px;height:1200px;overflow:hidden}
body{position:relative;background:var(--paper);font-family:"Noto Sans",sans-serif;color:var(--ink);font-size:9px}
.abs{position:absolute}
.heading{font-family:"Ubuntu",sans-serif;font-weight:700}

/* top strip */
.top-strip{left:0;top:0;width:1017px;height:20px;background:var(--lime)}
.utility-links{right:118px;top:5px;font-weight:700;font-size:9px;letter-spacing:.5px}
.utility-links span{margin:0 4px}

/* header */
.brand{left:116px;top:52px;font-family:"Ubuntu",sans-serif;font-weight:700;font-size:34px;line-height:40px;color:var(--turquoise)}
.header-ad{left:483px;top:34px;width:416px;height:80px;background:linear-gradient(100deg,#15181c 0%,#3a2e2e 55%,#8a1d1d 100%)}

/* nav */
.main-nav{left:0;top:124px;width:1017px;height:31px;background:var(--magenta)}
.main-nav a{position:absolute;top:8px;color:#fff;font-family:"Ubuntu",sans-serif;font-weight:700;font-size:11.5px;text-decoration:none;letter-spacing:.3px}
.main-nav .active{top:3px;left:135px;width:73px;height:24px;background:var(--lime);color:var(--ink);border-radius:3px;text-align:center;line-height:24px}
.nav-shadow{left:0;top:155px;width:1017px;height:26px;background:linear-gradient(#e6e6e6,#fafafa)}

/* hero */
.hero{left:0;top:181px;width:1017px;height:267px;background:radial-gradient(ellipse at 50% 40%,#8cc21c,var(--grass) 55%,var(--grass-dark))}
.section-title{color:#fff;font-size:14.5px;letter-spacing:.5px}
.card{background:var(--paper);border-radius:9px;box-shadow:4px 4px 0 #8c8c8c}
.search-card{left:117px;top:224px;width:396px;height:208px;background:linear-gradient(135deg,#fafafa,#ececec)}
.field-label{font-weight:700;font-size:9px;letter-spacing:.4px}
.field{width:203px;height:22px;border:1px solid #9a9a9a;background:#fff;color:#9a9a9a;font-size:8.5px;padding:5px 6px;letter-spacing:.3px}
.search-btn{left:86px;top:168px;width:58px;height:17px;background:var(--magenta);color:#fff;font-size:9px;text-align:center;line-height:17px}
.tagline{left:258px;top:67px;width:124px;text-align:center;font-family:"Ubuntu",sans-serif;font-weight:700;font-size:13.5px;line-height:17px}
.advance{left:262px;top:170px;font-weight:700;font-size:9px;letter-spacing:.6px;display:flex;align-items:center;gap:6px}
.employer-card{left:620px;top:221px;width:274px;height:208px}
.employer-mark{left:24px;top:17px;width:62px;height:62px;border:3px solid #d9181f;border-radius:6px}
.employer-name{left:112px;top:29px;font-size:10px}
.employer-copy{left:112px;top:47px;width:152px;font-size:8.2px;line-height:10.5px}
.read-more{font-weight:700;font-size:8.5px}
.other-label{left:17px;top:142px;font-size:10px}
.other-logos{left:17px;top:164px;width:246px;display:flex;justify-content:space-between;font-family:"Ubuntu",sans-serif;font-weight:700;font-size:22px;line-height:30px;color:#333}

/* latest jobs */
.latest-title{left:114px;top:475px;font-size:14.5px;color:var(--ink)}
.jobs-card{left:117px;top:506px;width:475px;height:348px;border:1px solid #ccc}
.tab{top:12px;height:19px;line-height:19px;color:#fff;background:#1f1f1f;text-align:center;font-size:9px;font-weight:700;border-radius:2px 2px 0 0}
.tab.on{background:var(--lime);color:var(--ink)}
.more-jobs{right:20px;top:17px;font-weight:700;font-size:8px;letter-spacing:.8px}
.jobs-table{left:13px;top:31px;width:448px;border-collapse:collapse;table-layout:fixed;background:var(--mist)}
.jobs-table td{height:48.3px;border-bottom:1px solid var(--rule);font-size:8.8px;vertical-align:middle;letter-spacing:.3px}
.jobs-table .title{display:block;font-weight:700;font-size:9px;letter-spacing:.6px}
.jobs-table .desc{display:block;width:130px;font-size:8px;line-height:9.5px}
.jobs-table .field-name{font-weight:700;letter-spacing:.8px}

/* feature tiles */
.tile{left:622px;width:277px;height:103px;border-radius:6px;color:#fff;box-shadow:2px -5px 0 #6f6f6f}
.tile h3{position:absolute;left:16px;font-family:"Ubuntu",sans-serif;font-weight:500;font-size:20px}
.tile p{position:absolute;left:16px;font-weight:700;font-size:8.5px;line-height:10.5px;letter-spacing:.3px}
.tile-blog{top:505px;background:var(--turquoise)}
.tile-article{top:626px;background:var(--magenta)}
.tile-podcast{top:746px;background:linear-gradient(90deg,#8a10a6,var(--purple) 60%,#b21cbe)}
.blog-square{left:180px;top:6px;width:91px;height:91px;border-radius:10px;background:#ff6d12}
.portrait{left:186px;top:7px;width:84px;height:89px;border:2px solid #fff;border-radius:4px;background:linear-gradient(160deg,#c9a48a,#8a6a58 60%,#3b3b3b)}
.podcast-art{left:172px;top:8px;width:96px;height:88px;border-radius:44px;background:radial-gradient(circle at 50% 50%,#ff8a1e 0 30%,#3c3c3c 31% 70%,transparent 71%)}

/* info boxes */
.info-box{top:873px;height:158px;background:var(--slate);color:#fff}
.info-box header{height:30px;background:var(--orange);padding:7px 11px;font-family:"Ubuntu",sans-serif;font-weight:500;font-size:14.5px}
.info-list{list-style:none;padding:8px 0 0 13px;font-weight:700;font-size:8.8px;line-height:14.5px;letter-spacing:.6px}
.info-list li::before{content:"-";margin-right:12px}
.scrollbar{right:0;top:30px;width:13px;height:128px;background:#f0f0f0;border-left:1px solid #bbb}
.scrollbar .thumb{position:absolute;left:2px;top:52px;width:9px;height:40px;background:#cdd8f0;border:1px solid #9aaad0;border-radius:2px}
.scrollbar .arrow{position:absolute;left:1px;width:11px;height:11px;background:#dfe6f6;border:1px solid #9aaad0}
.forum-copy{padding:13px 12px 0 12px;font-weight:700;font-size:8.8px;line-height:12.9px;letter-spacing:.55px}

/* bottom ads */
.ad-home{left:116px;top:1054px;width:474px;height:89px;background:linear-gradient(90deg,#1f4f8a,#5a8fb8 40%,#9cb0a0 70%,#e7e1d2)}
.ad-standout{left:622px;top:1054px;width:277px;height:89px;background:linear-gradient(100deg,#c8102e,#f04a5a 50%,#6a0a14)}

/* footer */
.footer{left:0;top:1171px;width:1017px;height:29px;background:var(--lime);text-align:center;line-height:29px;font-weight:700;font-size:9px;letter-spacing:.6px}
</style>
</head>
<body>

<div class="abs top-strip"></div>
<nav class="abs utility-links">Login<span>|</span>Register<span>|</span>Contact Us</nav>

<div class="abs brand">WorkHarbor.com</div>
<div class="abs header-ad" role="img" aria-label="Banner advertisement with dice, headline “Why Gamble? We’re a Sure Thing!”"></div>

<nav class="abs main-nav">
  <a class="active">HOME</a>
  <a style="left:260px">MY ACCOUNT</a>
  <a style="left:409px">FIND JOBS</a>
  <a style="left:537px">POST RESUME</a>
  <a style="left:680px">REGISTER</a>
  <a style="left:801px">EMPLOYER</a>
</nav>
<div class="abs nav-shadow"></div>

<section class="abs hero"></section>
<h2 class="abs heading section-title" style="left:116px;top:191px">JOB SEARCH</h2>
<h2 class="abs heading section-title" style="left:620px;top:191px">FEATURED EMPLOYER</h2>

<form class="abs card search-card">
  <div class="abs field-label" style="left:17px;top:21px">Job Title:</div>
  <div class="abs field" style="left:16px;top:32px">(e.g., nurse)</div>
  <div class="abs field-label" style="left:17px;top:69px">Skills/Keywords:</div>
  <div class="abs field" style="left:16px;top:80px">(e.g., healthcare, sales)</div>
  <div class="abs field-label" style="left:17px;top:117px">Location:</div>
  <div class="abs field" style="left:16px;top:128px">(city, state, or zip code)</div>
  <div class="abs search-btn">Search</div>
  <div class="abs tagline">“FIND THE JOB YOU DESERVE MOST”</div>
  <div class="abs advance">Advance Search
    <svg width="13" height="13" viewBox="0 0 13 13"><circle cx="6.5" cy="6.5" r="6.5" fill="#1a1a1a"/><path d="M3.5 5l3 3 3-3" stroke="#fff" stroke-width="1.6" fill="none"/></svg>
  </div>
</form>

<aside class="abs card employer-card">
  <div class="abs employer-mark"></div>
  <div class="abs employer-name">Harborline Mutual</div>
  <p class="abs employer-copy">Lorem Ipsum is simply dummy text of the printing and typesetting industry. Lorem Ipsum has been the industry's standard dummy text ever since the 1500s.</p>
  <div class="abs read-more" style="left:205px;top:113px">Read More</div>
  <div class="abs other-label">Other Employers</div>
  <div class="abs other-logos"><span>Verano</span><span>Quorra</span><span>Bexley</span></div>
</aside>

<h2 class="abs heading latest-title">LATEST JOBS</h2>
<section class="abs card jobs-card">
  <div class="abs tab on" style="left:13px;width:106px">By Area of Interest</div>
  <div class="abs tab" style="left:125px;width:106px">By Field</div>
  <div class="abs tab" style="left:237px;width:106px">By Qualification</div>
  <div class="abs more-jobs">MORE JOBS</div>
  <table class="abs jobs-table">
    <colgroup><col style="width:83px"><col style="width:155px"><col style="width:66px"><col style="width:76px"><col style="width:68px"></colgroup>
    <tr><td style="padding-left:9px">April 05</td><td><span class="title">Data Entry</span><span class="desc">Lorem Ipsum is simply dummy text of the printing</span></td><td>Tresla</td><td class="field-name">Computer</td><td>$10/Hour</td></tr>
    <tr><td style="padding-left:9px">April 05</td><td><span class="title">Lorum Ipsum</span><span class="desc">Lorem Ipsum is simply dummy text of the printing</span></td><td>Tresla</td><td class="field-name">Demo</td><td>$10/Hour</td></tr>
    <tr><td style="padding-left:9px">April 05</td><td><span class="title">Lorum Ipsum</span><span class="desc">Lorem Ipsum is simply dummy text of the printing</span></td><td>Tresla</td><td class="field-name">Demo</td><td>$10/Hour</td></tr>
    <tr><td style="padding-left:9px">April 05</td><td><span class="title">Lorum Ipsum</span><span class="desc">Lorem Ipsum is simply dummy text of the printing</span></td><td>Tresla</td><td class="field-name">Demo</td><td>$10/Hour</td></tr>
    <tr><td style="padding-left:9px">April 05</td><td><span class="title">Lorum Ipsum</span><span class="desc">Lorem Ipsum is simply dummy text of the printing</span></td><td>Tresla</td><td class="field-name">Demo</td><td>$10/Hour</td></tr>
    <tr><td style="padding-left:9px">April 05</td><td><span class="title">Lorum Ipsum</span><span class="desc">Lorem Ipsum is simply dummy text of the printing</span></td><td>Tresla</td><td class="field-name">Demo</td><td>$10/Hour</td></tr>
  </table>
</section>

<article class="abs tile tile-blog">
  <h3 style="top:10px">Our blog</h3>
  <p style="top:44px;width:155px">Lorem Ipsum is simply dummy text of the printing and typesetting industry.</p>
  <p style="top:86px">Read More</p>
  <div class="abs blog-square"></div>
</article>

<article class="abs tile tile-article">
  <h3 style="top:10px">Latest Article</h3>
  <p style="top:44px;width:165px">Dana R.<br>Lorem Ipsum is simply dummy text of the printing and typesetting industry.</p>
  <p style="top:90px">Read More</p>
  <div class="abs portrait" role="img" aria-label="Portrait photo of the article author"></div>
</article>

<article class="abs tile tile-podcast">
  <h3 style="top:36px;left:19px;line-height:23px">Listen Live<br>Our Podcasts</h3>
  <div class="abs podcast-art" role="img" aria-label="Illustration of headphones around a podcast feed icon"></div>
</article>

<section class="abs info-box" style="left:116px;width:249px">
  <header>List of Jobs</header>
  <ul class="info-list">
    <li>Accounts</li><li>Audits</li><li>Computer Software</li><li>Computer Data Entry</li><li>Graphic Designing</li><li>Logo Designing</li><li>S.E.O.</li><li>Web Designing</li>
  </ul>
  <div class="abs scrollbar"><div class="arrow" style="top:1px"></div><div class="thumb"></div><div class="arrow" style="bottom:1px"></div></div>
</section>

<section class="abs info-box" style="left:378px;width:254px">
  <header>Work Harbor Forum</header>
  <p class="forum-copy">Lorem Ipsum is simply dummy text of the printing and typesetting industry. Lorem Ipsum has been the industry's standard dummy text ever since the 1500s, when an unknown printer took a galley of type and scrambled it to make a type specimen book.</p>
  <div class="abs read-more" style="left:170px;top:135px;font-size:8.8px;letter-spacing:.6px">Read More</div>
</section>

<section class="abs info-box" style="left:644px;width:255px">
  <header>Employers List</header>
  <ul class="info-list">
    <li>JS Designs</li><li>Atlantis &amp; Co</li><li>Pixel Assembly</li><li>Freelance</li><li>Keystone Property Care</li><li>Web Portal</li><li>Online Work Portal</li><li>Global Computers</li>
  </ul>
  <div class="abs scrollbar"><div class="arrow" style="top:1px"></div><div class="thumb"></div><div class="arrow" style="bottom:1px"></div></div>
</section>

<div class="abs ad-home" role="img" aria-label="Banner advertisement: “New Home… New Life Style” over a lakeside scene for Lakeview Residences"></div>
<div class="abs ad-standout" role="img" aria-label="Banner advertisement: “We Stand Out from the Rest” in hand-lettered type"></div>

<footer class="abs footer">©2010 workharbor.com - All Rights Reserved</footer>

</body>
</html>
```